Velor Crest Banners

We need banners for our website VelorCrest.com.
The Design must include "The Secret Japanese Skin Care System For Flawless Skin". We will need four banner sizes 300x250, 180x150, 160x600, 728x90, with our logo.

Industry/Entity Type

Paint

```html
<!DOCTYPE html>
<html lang="en">
<head>
<meta charset="utf-8">
<title>Velor Crest Banners</title>
<link rel="stylesheet" href="https://fonts.googleapis.com/css2?family=Lato:wght@400;700&family=Lora:ital@1&family=Playball&display=swap">
<style>
  :root {
    --page: #ffffff;
    --ink: #1c1c1c;
    --magenta: #d4127c;
    --magenta-deep: #c40f72;
    --pink: #ea1c86;
    --panel: #ececec;
    --panel-light: #f7f7f7;
    --rule: #9a9a9a;
    --frame: #3a3a3a;
    --call-bg: #0d0d0d;
    --white: #ffffff;
    --note: #222222;
    --swoosh: #c8c8c8;
  }
  * { box-sizing: border-box; margin: 0; padding: 0; }
  html, body { width: 1200px; height: 1114px; overflow: hidden; background: var(--page); }
  body { position: relative; font-family: "Lato", Arial, sans-serif; color: var(--ink); }

  .banner {
    position: absolute;
    overflow: hidden;
    border: 1px solid var(--frame);
    background: radial-gradient(ellipse at 40% 60%, var(--panel-light), var(--panel));
  }
  .banner svg { position: absolute; display: block; }

  .brand { position: absolute; display: flex; flex-direction: column; align-items: center; }
  .brand-mark { background: var(--ink); }
  .brand-name { font-family: "Lato", Arial, sans-serif; font-weight: 400; color: var(--ink); letter-spacing: 3px; white-space: nowrap; text-transform: uppercase; }

  .ask { position: absolute; font-family: "Lato", Arial, sans-serif; color: var(--magenta); text-align: center; line-height: 1.3; }
  .rule { position: absolute; height: 2px; background: var(--rule); }
  .pitch { position: absolute; font-family: "Lora", Georgia, serif; font-style: italic; text-align: center; color: var(--ink); line-height: 1.22; }
  .promise { position: absolute; font-family: "Playball", cursive; color: var(--ink); text-align: center; line-height: 1.05; text-shadow: 0 2px 3px rgba(0,0,0,.18); }
  .cta {
    position: absolute; background: var(--magenta-deep); color: var(--white);
    font-family: "Lato", Arial, sans-serif; font-weight: 400;
    display: flex; align-items: center; justify-content: center; border: 2px solid var(--white);
  }
  .call {
    position: absolute; background: var(--call-bg); color: var(--white);
    font-family: "Lato", Arial, sans-serif; display: flex; align-items: center; justify-content: center;
  }

  /* notes */
  .note { position: absolute; right: 45px; font-family: "Lora", Georgia, serif; font-style: italic; font-size: 29px; color: var(--note); text-align: right; white-space: nowrap; }
  .note-swoosh { position: absolute; }

  /* skyscraper 160x600 */
  .sky { left: 46px; top: 27px; width: 243px; height: 904px; }
  .sky .brand { left: 0; right: 0; top: 22px; }
  .sky .brand-mark { width: 40px; height: 40px; margin-bottom: 10px; }
  .sky .brand-name { font-size: 25px; }
  .sky .ask { left: 0; right: 0; top: 464px; font-size: 28px; }
  .sky .rule { left: 24px; right: 24px; top: 550px; }
  .sky .pitch { left: 0; right: 0; top: 566px; font-size: 24px; line-height: 1.42; }
  .sky .promise { left: 0; right: 0; top: 676px; font-size: 58px; line-height: 1.05; }
  .sky .cta { left: 22px; width: 196px; top: 803px; height: 48px; font-size: 27px; }
  .sky .call { left: 0; right: 0; bottom: 0; height: 38px; font-size: 22px; }

  /* medium rectangle 300x250 (base), small 180x150 scaled */
  .rect { width: 453px; height: 378px; }
  .rect .inner { position: absolute; left: 0; top: 0; width: 451px; height: 376px; transform-origin: 0 0; }
  .rect-md { left: 316px; top: 294px; }
  .rect-sm { left: 316px; top: 702px; width: 273px; height: 229px; }
  .rect-sm .inner { transform: scale(0.6); }
  .rect .brand { left: 0; width: 232px; top: 12px; }
  .rect .brand-mark { width: 32px; height: 32px; margin-bottom: 6px; }
  .rect .brand-name { font-size: 22px; }
  .rect .ask { left: 0; width: 232px; top: 98px; font-size: 26px; line-height: 1.32; }
  .rect .rule { left: 30px; width: 176px; top: 174px; }
  .rect .pitch { left: 0; width: 238px; top: 182px; font-size: 22px; line-height: 1.3; }
  .rect .promise { left: 0; width: 236px; top: 278px; font-size: 46px; line-height: 1.06; }
  .rect .cta { left: 271px; width: 175px; top: 296px; height: 42px; font-size: 24px; }
  .rect .call { left: 254px; right: 0; bottom: 0; height: 34px; font-size: 20px; }

  /* leaderboard 728x90 */
  .board { left: 46px; top: 952px; width: 1095px; height: 137px; }
  .board .brand { left: 0; width: 100px; top: 20px; }
  .board .brand-mark { width: 36px; height: 36px; margin-bottom: 8px; }
  .board .brand-name { font-size: 20px; white-space: normal; text-align: center; line-height: 1.2; width: 100px; }
  .board .ask { left: 315px; width: 180px; top: 26px; font-size: 26px; line-height: 1.3; }
  .board .divider { position: absolute; left: 511px; top: 20px; width: 1px; height: 100px; background: var(--rule); }
  .board .pitch { left: 540px; width: 350px; top: 6px; font-size: 24px; line-height: 1.38; }
  .board .promise { left: 540px; width: 350px; top: 74px; font-size: 46px; }
  .board .cta { left: 925px; width: 160px; top: 62px; height: 42px; font-size: 24px; }
  .board .call { left: 894px; right: 0; top: 0; height: 32px; font-size: 21px; }
</style>
</head>
<body>

  <p class="note" style="top:38px;">Simple Yet Effective</p>
  <svg class="note-swoosh" style="left:1060px;top:78px;" width="110" height="18" viewBox="0 0 110 18"><path d="M4 16 C40 4 80 2 108 4 C80 6 44 10 4 16Z" fill="var(--swoosh)"/></svg>
  <p class="note" style="top:102px;">Web based color used</p>
  <svg class="note-swoosh" style="left:1040px;top:138px;" width="120" height="32" viewBox="0 0 120 32"><path d="M4 30 C30 12 70 4 118 2 C76 8 40 16 4 30Z" fill="var(--swoosh)"/></svg>

  <!-- Skyscraper -->
  <section class="banner sky">
    <div class="brand"><span class="brand-mark"></span><span class="brand-name">Velor Crest</span></div>
    <svg style="left:0;top:123px;" width="241" height="340" viewBox="0 0 241 340">
      <defs>
        <linearGradient id="skyPhoto" x1="0" y1="0" x2="1" y2="1">
          <stop offset="0" stop-color="#7c4a2e"/><stop offset=".45" stop-color="#e3b796"/><stop offset="1" stop-color="#f3efec"/>
        </linearGradient>
      </defs>
      <path d="M0 0H241V250C190 300 100 300 0 245Z" fill="url(#skyPhoto)" role="img" aria-label="Portrait photograph of a woman resting her head on her arms"/>
      <path d="M0 255C90 312 180 312 241 262V282C180 338 80 336 0 282Z" fill="var(--pink)"/>
    </svg>
    <p class="ask">Do you want<br>Beautiful Skin?</p>
    <div class="rule"></div>
    <p class="pitch">Here Is The Secret<br>Japanese Skin Care<br>System For</p>
    <p class="promise">Flawless<br>Skin</p>
    <div class="cta">LEARN MORE</div>
    <div class="call">Call: 888-555-0142</div>
  </section>

  <!-- Medium rectangle and small rectangle -->
  <section class="banner rect rect-md">
    <div class="inner">
      <svg style="left:0;top:0;" width="451" height="376" viewBox="0 0 451 376">
        <defs>
          <linearGradient id="mdPhoto" x1="0" y1="0" x2="1" y2="1">
            <stop offset="0" stop-color="#7c4a2e"/><stop offset=".5" stop-color="#e2b595"/><stop offset="1" stop-color="#f3efec"/>
          </linearGradient>
        </defs>
        <path d="M228 0H451V376H262C262 250 248 120 228 0Z" fill="url(#mdPhoto)" role="img" aria-label="Portrait photograph of a woman resting her head on her arms"/>
        <path d="M204 0H228C248 120 262 250 262 376H246C246 250 228 120 204 0Z" fill="var(--pink)"/>
      </svg>
      <div class="brand"><span class="brand-mark"></span><span class="brand-name">Velor Crest</span></div>
      <p class="ask">Do you want<br>Beautiful Skin?</p>
      <div class="rule"></div>
      <p class="pitch">Here Is The Secret<br>Japanese Skin Care<br>System For</p>
      <p class="promise">Flawless<br>Skin</p>
      <div class="cta">LEARN MORE</div>
      <div class="call">Call: 888-555-0142</div>
    </div>
  </section>

  <section class="banner rect rect-sm">
    <div class="inner">
      <svg style="left:0;top:0;" width="451" height="376" viewBox="0 0 451 376">
        <defs>
          <linearGradient id="smPhoto" x1="0" y1="0" x2="1" y2="1">
            <stop offset="0" stop-color="#7c4a2e"/><stop offset=".5" stop-color="#e2b595"/><stop offset="1" stop-color="#f3efec"/>
          </linearGradient>
        </defs>
        <path d="M228 0H451V376H262C262 250 248 120 228 0Z" fill="url(#smPhoto)" role="img" aria-label="Portrait photograph of a woman resting her head on her arms"/>
        <path d="M204 0H228C248 120 262 250 262 376H246C246 250 228 120 204 0Z" fill="var(--pink)"/>
      </svg>
      <div class="brand"><span class="brand-mark"></span><span class="brand-name">Velor Crest</span></div>
      <p class="ask">Do you want<br>Beautiful Skin?</p>
      <div class="rule"></div>
      <p class="pitch">Here Is The Secret<br>Japanese Skin Care<br>System For</p>
      <p class="promise">Flawless<br>Skin</p>
      <div class="cta">LEARN MORE</div>
      <div class="call">Call: 888-555-0142</div>
    </div>
  </section>

  <!-- Leaderboard -->
  <section class="banner board">
    <svg style="left:0;top:0;" width="1093" height="135" viewBox="0 0 1093 135">
      <defs>
        <linearGradient id="boardPhoto" x1="0" y1="0" x2="1" y2="1">
          <stop offset="0" stop-color="#7c4a2e"/><stop offset=".5" stop-color="#e2b595"/><stop offset="1" stop-color="#f3efec"/>
        </linearGradient>
      </defs>
      <path d="M100 0H284C300 40 304 95 294 135H100Z" fill="url(#boardPhoto)" role="img" aria-label="Portrait photograph of a woman resting her head on her arms"/>
      <path d="M284 0H300C318 40 320 95 310 135H294C304 95 300 40 284 0Z" fill="var(--pink)"/>
    </svg>
    <div class="brand"><span class="brand-mark"></span><span class="brand-name">Velor<br>Crest</span></div>
    <p class="ask">Do you want<br>Beautiful Skin?</p>
    <div class="divider"></div>
    <p class="pitch">Here Is The Secret Japanese<br>Skin Care System For</p>
    <p class="promise">Flawless Skin</p>
    <div class="call">Call: 888-555-0142</div>
    <div class="cta">LEARN MORE</div>
  </section>

</body>
</html>
```